Classic Minimalistic Business Card

Design a classic, minimalistic Business Card. Please find inspiration in the attached Classic Minimalistic examples. My information:
Name: Glen Ovamir
Company: Ovamir Capital
Logo: OC
Address: 1470 N Thornwick Rd, Suite 210 | Maplecrest, IL 60199
Phone: 630-555-0192
Email: glenovamir@pvt.insure
Slogan: Building Strength Through Capital

Feel free to leave out any of the information above except my name.

I have selected Double-sided, but I am also open to Single-sided

Target Market(s)

22-70. income greater than 150k/year

Industry/Entity Type

Finance

Contact Information for Business Card

See Project Description

Requirements
Must have
• Ivory or "antiqued" background similar to the reference pictures

```html
<!DOCTYPE html>
<html lang="en">
<head>
<meta charset="utf-8">
<title>Ovamir Capital — Business Card</title>
<link rel="stylesheet" href="https://fonts.googleapis.com/css2?family=Cinzel&family=Josefin+Sans:wght@600&family=Pinyon+Script&display=swap">
<style>
  :root {
    --page: #ffffff;
    --paper-light: #f4e8c8;
    --paper-mid: #efdfb5;
    --paper-dark: #e9d6a6;
    --ink: #16130f;
    --rule: #8e959c;
  }
  * { margin: 0; padding: 0; box-sizing: border-box; }
  html, body {
    width: 960px;
    height: 1200px;
    overflow: hidden;
    background: var(--page);
  }
  .canvas {
    position: relative;
    width: 960px;
    height: 1200px;
  }
  .card {
    position: absolute;
    left: 162px;
    width: 637px;
    height: 302px;
    background:
      radial-gradient(ellipse at 30% 25%, var(--paper-light) 0%, transparent 60%),
      radial-gradient(ellipse at 80% 90%, var(--paper-dark) 0%, transparent 65%),
      var(--paper-mid);
    color: var(--ink);
    text-align: center;
  }
  .card--front { top: 266px; }
  .card--back { top: 632px; }

  .brand {
    position: absolute;
    top: 104px;
    left: 0;
    right: 0;
    display: flex;
    justify-content: center;
    align-items: center;
    gap: 16px;
  }
  .brand__dot {
    width: 46px;
    height: 46px;
    border-radius: 50%;
    background: var(--ink);
  }
  .brand__name {
    font-family: "Josefin Sans", sans-serif;
    font-weight: 600;
    font-size: 29px;
    line-height: 30px;
    letter-spacing: 1px;
    text-align: left;
    padding-top: 6px;
  }
  .tagline {
    position: absolute;
    top: 221px;
    left: 0;
    right: 0;
    font-family: "Cinzel", serif;
    font-size: 17.5px;
    line-height: 21px;
    letter-spacing: 1.8px;
  }

  .holder {
    position: absolute;
    top: 38px;
    left: 0;
    right: 0;
    font-family: "Pinyon Script", cursive;
    font-weight: 400;
    font-size: 50px;
    line-height: 64px;
  }
  .holder-rule {
    position: absolute;
    top: 121px;
    left: 172px;
    width: 292px;
    height: 1px;
    background: var(--rule);
  }
  .contact {
    position: absolute;
    left: 0;
    right: 0;
    font-family: "Cinzel", serif;
    font-size: 20.5px;
    letter-spacing: 1.8px;
    line-height: 20px;
  }
  .contact--address { top: 152px; }
  .contact--phone { top: 203px; }
  .contact--email { top: 234px; }
</style>
</head>
<body>
<main class="canvas">
  <section class="card card--front">
    <div class="brand">
      <span class="brand__dot" aria-hidden="true"></span>
      <div class="brand__name">OVAMIR<br>CAPITAL</div>
    </div>
    <p class="tagline">BUILDING STRENGTH<br>THROUGH CAPITAL</p>
  </section>

  <section class="card card--back">
    <h1 class="holder">Glen Ovamir</h1>
    <div class="holder-rule"></div>
    <p class="contact contact--address">1470 N THORNWICK RD,<br>SUITE 210 | MAPLECREST, IL 60199</p>
    <p class="contact contact--phone">630-555-0192</p>
    <p class="contact contact--email">GLENOVAMIR@PVT.INSURE</p>
  </section>
</main>
</body>
</html>
```